Need new sign at entrance for new fruit and vegetable wholesaler in market. Main vegetables sold are
Broccoli , Cauliflower , cabbage , capsicum , tomatoes , lettuce .
Business name is Tall Meadow
I have included examples of other designs and a sketch of suggested layout.

```html
<!DOCTYPE html>
<html lang="en">
<head>
<meta charset="utf-8">
<title>Tall Meadow – Entrance Sign</title>
<link rel="stylesheet" href="https://fonts.googleapis.com/css2?family=Tenor+Sans&family=PT+Sans&display=swap">
<style>
  :root {
    --sign-bg: #ffffff;
    --brand-green: #8cc63f;
    --contact-ink: #1a1a1a;
    --url-green: #5aa02c;
    --produce-light: #a6cf6a;
    --produce-deep: #5f8f3a;
  }
  html, body {
    margin: 0;
    padding: 0;
    overflow: hidden;
    background: var(--sign-bg);
  }
  .sign {
    position: relative;
    width: 1200px;
    height: 240px;
    overflow: hidden;
    background: var(--sign-bg);
  }
  .location,
  .contact {
    position: absolute;
    top: 19px;
    margin: 0;
    font-family: "PT Sans", sans-serif;
    font-size: 16px;
    line-height: 21px;
    color: var(--contact-ink);
  }
  .location { left: 26px; }
  .contact { right: 24px; text-align: left; }
  .contact .web { color: var(--url-green); display: block; margin-top: 6px; }
  .business-name {
    position: absolute;
    left: 0;
    right: 0;
    top: 20px;
    margin: 0;
    text-align: center;
    font-family: "Tenor Sans", sans-serif;
    font-weight: 400;
    font-size: 100px;
    line-height: 100px;
    letter-spacing: 1px;
    color: var(--brand-green);
  }
  .produce-area {
    position: absolute;
    left: 0;
    bottom: 0;
    width: 1200px;
    height: 100px;
    background: linear-gradient(to bottom, var(--produce-light), var(--produce-deep));
  }
</style>
</head>
<body>
  <div class="sign">
    <p class="location">Stand 214<br>C Shed</p>

    <h1 class="business-name">TALL MEADOW</h1>

    <p class="contact">
      Ph: 03-9876-5410<br>
      Fx: 03-9876-5410
      <span class="web">tallmeadow.com.au</span>
    </p>

    <div class="produce-area" role="img"
         aria-label="Photo row of fresh vegetables: capsicums, broccoli, cabbage, tomatoes and lettuce"></div>
  </div>
</body>
</html>
```